Business Cards

Business cards (double-sided) to be handed out to clients and potential clients, with contact details, logo .

Target Market(s)

Small to medium size businesses

Industry/Entity Type

Accountants

Contact Information for Business Card

Brightwater Ledger & Counsel Ltd

Colors

Designer to choose only greyscale colors for use in the design.

Requirements
Must have
• Name, Title, Address, Phone number, Email, Website
Nice to have
• Modern, clean lines, classy
Should not have
• Business cards to be double-sided. Form keeps reverting to single-sided.

```html
<!DOCTYPE html>
<html lang="en">
<head>
<meta charset="utf-8">
<title>Brightwater Ledger &amp; Counsel – Business Cards</title>
<link rel="stylesheet" href="https://fonts.googleapis.com/css2?family=Jost:wght@300;400;600&display=swap">
<style>
  :root {
    --stage: #000000;
    --card-front: #646464;
    --card-back: #ffffff;
    --mark-dark: #3e3e3e;
    --ink-grey: #8c8c8c;
  }
  * { margin: 0; padding: 0; box-sizing: border-box; }
  html, body {
    width: 1200px; height: 1000px; overflow: hidden;
    background: var(--stage);
    font-family: "Jost", sans-serif;
  }
  .stage { position: relative; width: 1200px; height: 1000px; }
  .card {
    position: absolute; left: 343px; width: 514px; height: 297px;
  }
  .card--front {
    top: 197px; background: var(--card-front);
    display: flex; align-items: center; justify-content: center;
  }
  .card--back {
    top: 579px; background: var(--card-back);
    box-shadow: 0 30px 60px rgba(255,255,255,0.06);
  }
  .wordmark {
    font-family: "Jost", sans-serif;
    font-weight: 400;
    text-transform: uppercase;
    letter-spacing: 0.14em;
    line-height: 1.15;
  }
  .card--front .wordmark {
    color: var(--mark-dark); font-size: 19px; text-align: center;
    transform: translate(10px, 0);
  }
  .card--back .wordmark {
    position: absolute; top: 616px; right: 0;
    color: var(--ink-grey); font-size: 15px; text-align: right;
  }
  .card--back .wordmark { top: 36px; right: 37px; }
  .holder { position: absolute; left: 42px; top: 70px; color: var(--ink-grey); }
  .holder__name { font-weight: 600; font-size: 17px; line-height: 20px; }
  .holder__title { font-weight: 300; font-size: 16px; line-height: 20px; margin-top: 1px; }
  .contact { position: absolute; left: 40px; color: var(--ink-grey); font-weight: 300; font-size: 16px; }
  .contact li { list-style: none; display: flex; align-items: center; height: 21.5px; }
  .contact svg { width: 14px; height: 14px; margin-right: 6px; fill: var(--ink-grey); flex: none; }
  .contact--place { top: 150px; }
  .contact--reach { top: 193px; }
</style>
</head>
<body>
<main class="stage">
  <section class="card card--front" aria-label="Card front">
    <p class="wordmark">Brightwater<br>Ledger &amp; Counsel</p>
  </section>

  <section class="card card--back" aria-label="Card back">
    <p class="wordmark">Brightwater<br>Ledger &amp; Counsel</p>

    <div class="holder">
      <p class="holder__name">Name Surname</p>
      <p class="holder__title">Title</p>
    </div>

    <ul class="contact contact--place">
      <li>
        <svg viewBox="0 0 14 14"><path d="M7 0.5a4.6 4.6 0 0 0-4.6 4.6C2.4 8.5 7 13.5 7 13.5s4.6-5 4.6-8.4A4.6 4.6 0 0 0 7 0.5zm0 6.4a1.8 1.8 0 1 1 0-3.6 1.8 1.8 0 0 1 0 3.6z"/></svg>
        Address
      </li>
    </ul>

    <ul class="contact contact--reach">
      <li>
        <svg viewBox="0 0 14 14"><path d="M3.2 1.5l2 2.4-1.1 1.4c.8 1.7 2 2.9 3.7 3.7l1.4-1.1 2.4 2-1.2 1.8C6.5 11.6 2.4 7.5 1.5 3z"/></svg>
        Phone number
      </li>
      <li>
        <svg viewBox="0 0 14 14"><path d="M1.5 3.5h11v7h-11z M1.5 3.5L7 7.8l5.5-4.3" fill="none" stroke="#8c8c8c" stroke-width="1.3"/><path d="M1.5 3.5h11L7 7.5z"/></svg>
        Email
      </li>
      <li>
        <svg viewBox="0 0 14 14"><g fill="none" stroke="#8c8c8c" stroke-width="1.1"><circle cx="7" cy="7" r="5.6"/><ellipse cx="7" cy="7" rx="2.4" ry="5.6"/><path d="M1.4 7h11.2M2.3 4.2h9.4M2.3 9.8h9.4"/></g></svg>
        Website
      </li>
    </ul>
  </section>
</main>
</body>
</html>
```